Envelope Design Project for Real Estate

I am looking for an envelope design for a real estate brokerage. I prefer muted colors and the primary colors should be white, maroon (884445) and gray (aaaaaa).
The design is for a #10 universal envelope (psd and jpg files attached for guidelines). There should be full color on the front and back of the envelope.
You can add a return address on the back side along the top flap. Please use a sample address and phone number in the design - the actual information will be provided to the winning designer.

```html
<!DOCTYPE html>
<html lang="en">
<head>
<meta charset="utf-8">
<title>Stone Harbor Realty – #10 Envelope</title>
<link rel="stylesheet" href="https://fonts.googleapis.com/css2?family=Cinzel:wght@400;600&family=Cormorant+Garamond:ital,wght@1,600&display=swap">
<style>
  :root {
    --backdrop: #a87c25;
    --maroon: #884445;
    --maroon-dark: #6e3536;
    --gray: #aaaaaa;
    --gray-flap: #9a9a9a;
    --white: #ffffff;
    --paper-edge: #f3f0f0;
    --guide-green: #4caf50;
    --guide-teal: #7fd3c8;
    --cut-line: #ffffff;
    --watermark: #f1ecec;
  }
  html, body {
    margin: 0;
    padding: 0;
    width: 1200px;
    height: 686px;
    overflow: hidden;
    background: var(--backdrop);
  }
  .envelope-sheet {
    display: block;
    width: 1200px;
    height: 686px;
  }
  .sc-text {
    font-family: "Cinzel", "Times New Roman", serif;
    font-weight: 400;
  }
  .brand-name {
    font-family: "Cinzel", "Times New Roman", serif;
    font-weight: 600;
  }
  .mobile-label {
    font-family: "Cormorant Garamond", "Times New Roman", serif;
    font-style: italic;
    font-weight: 600;
  }
</style>
</head>
<body>
<svg class="envelope-sheet" viewBox="0 0 1200 686" xmlns="http://www.w3.org/2000/svg">
  <rect class="backdrop" width="1200" height="686" fill="var(--backdrop)"/>

  <!-- die cut outline -->
  <path class="cut-line" d="M300 55 Q302 50 312 50 L852 50 Q864 50 868 62 L878 138 L915 140 Q938 142 938 165 L938 380 Q936 400 910 404 L880 408 L872 602 Q868 640 850 640 L300 640 Q282 640 280 602 L276 408 L240 404 Q214 400 214 380 L214 165 Q214 142 238 140 L272 138 Z"
        fill="none" stroke="var(--cut-line)" stroke-width="1.3" stroke-dasharray="5 4"/>

  <!-- side flaps -->
  <g class="side-flap side-flap--left">
    <path d="M282 145 L245 145 Q222 147 222 170 L222 375 Q224 395 245 398 L282 405 Z" fill="var(--white)"/>
    <path d="M222 196 L252 196 Q262 196 262 208 L262 395 L245 398 Q224 395 222 375 Z" fill="var(--gray-flap)"/>
  </g>
  <g class="side-flap side-flap--right">
    <path d="M872 145 L910 145 Q932 147 932 170 L932 375 Q930 395 910 398 L872 405 Z" fill="var(--white)"/>
    <path d="M932 196 L904 196 Q894 196 894 208 L894 395 L910 398 Q930 395 932 375 Z" fill="var(--gray-flap)"/>
  </g>

  <!-- top flap with return address -->
  <path class="top-flap" d="M300 72 Q302 60 316 60 L846 60 Q858 60 860 72 L872 150 L282 150 Z" fill="var(--maroon)"/>
  <path class="guide guide--top" d="M310 72 L850 72 L860 135 L298 135 Z" fill="none" stroke="var(--guide-green)" stroke-width="0.8" opacity="0.7"/>
  <text class="sc-text return-address" x="578" y="110" text-anchor="middle" font-size="10" fill="var(--white)" letter-spacing="0.4">COMPLEX NAME,STREET NAME CITY, STATE, ZIP CODE</text>

  <!-- front panel -->
  <g class="front-panel">
    <rect x="282" y="145" width="590" height="256" fill="var(--white)"/>
    <rect class="front-band" x="282" y="145" width="590" height="65" fill="var(--maroon)"/>
    <rect class="front-band-rule" x="282" y="210" width="590" height="4" fill="var(--gray)"/>
    <rect class="window-pattern" x="715" y="145" width="157" height="62" fill="var(--maroon-dark)" opacity="0.35" role="img" aria-label="Decorative pattern of small window squares"/>
    <text class="sc-text website" x="822" y="188" text-anchor="end" font-size="9.5" fill="var(--white)" letter-spacing="0.5">WWW.HARBORHOMEGUIDE.COM</text>

    <rect class="guide guide--front" x="294" y="158" width="566" height="232" fill="none" stroke="var(--guide-teal)" stroke-width="0.8"/>

    <!-- brand arch -->
    <path class="brand-arch" d="M340 212 Q345 186 396 184 Q447 186 452 212" fill="var(--white)" stroke="var(--gray)" stroke-width="3"/>
    <circle class="brand-dot" cx="396" cy="233" r="30" fill="var(--maroon)"/>
    <text class="brand-name" x="396" y="285" text-anchor="middle" font-size="19" fill="var(--maroon)">STONE HARBOR</text>
    <text class="brand-name" x="396" y="300" text-anchor="middle" font-size="11" fill="var(--maroon)" letter-spacing="3">REALTY</text>

    <text class="sc-text address-line" x="392" y="315" text-anchor="middle" font-size="8.6" fill="#222">COMPLEX NAME,STREET NAME</text>
    <text class="sc-text address-line" x="392" y="325" text-anchor="middle" font-size="8.6" fill="#222">CITY, STATE, ZIP CODE</text>
    <text x="392" y="339" text-anchor="middle" font-size="8.6" fill="#222">
      <tspan class="mobile-label" fill="var(--maroon)" font-size="9.5">Mobile</tspan><tspan class="sc-text"> : (555) 014-2290</tspan>
    </text>

    <!-- faint brand watermark -->
    <circle class="brand-watermark" cx="768" cy="322" r="62" fill="var(--watermark)"/>
  </g>

  <!-- bottom flap -->
  <path class="bottom-flap" d="M282 401 L872 401 L862 600 Q860 620 842 622 L306 622 Q288 620 288 600 Z" fill="var(--maroon)"/>
  <path class="guide guide--bottom" d="M294 414 L858 414 L850 556 L302 556 Z" fill="none" stroke="var(--guide-green)" stroke-width="0.8" opacity="0.7"/>
  <g class="brand-flipped" transform="rotate(180 564 478)">
    <circle cx="564" cy="460" r="42" fill="var(--white)"/>
    <text class="brand-name" x="564" y="528" text-anchor="middle" font-size="22" fill="var(--white)">STONE HARBOR</text>
    <text class="brand-name" x="564" y="544" text-anchor="middle" font-size="12" fill="var(--white)" letter-spacing="3">REALTY</text>
  </g>

  <!-- glue strip -->
  <path class="glue-strip" d="M318 578 L836 578 Q842 578 844 586 L852 634 L302 634 L312 586 Q314 578 318 578 Z" fill="var(--gray-flap)"/>
</svg>
</body>
</html>
```